Kestrel Building Works Business Card and more!

We need a business card design for Kestrel Building Works Ltd, a respected building company that specialises in high quality designer homes.

We're after a sleek, clean, modern business card that incorporates our new logo (see attached) and colours, with black being the background.

We are Certified Framing Guild and need to include their logo (see attached) on our cards, balancing but not taking over our logo.

Details to be included:

Malcolm Tivey
Director

Phone: 0218845126
Email: kestrelbuild.nz@maildrop-example.co.nz
Website: www.kestrelbuildingworks-example.co.nz

Additional Information

A start up website is also under construction and needing attention and letterheads are needed!

We look forward to your designs!

Target Market(s)

30+ people who are interested in building new or renovating current homes

Industry/Entity Type

Construction

Contact Information for Business Card

Malcolm Tivey
Director

Phone: 0218845126
Facebook: www.socialpage-example.com/kestrelbuild.nz

Font styles to use
Serif

Colors

Designer to choose colors to be used in the design.

Requirements
Must have
• Our new logo
• Our colours
• cfg logo

```html
<!DOCTYPE html>
<html lang="en">
<head>
<meta charset="utf-8">
<title>Kestrel Building Works – Business Card</title>
<link rel="stylesheet" href="https://fonts.googleapis.com/css2?family=Cinzel:wght@600&family=Roboto:wght@400;700&display=swap">
<style>
  :root {
    --bg: #e4e4e4;
    --ink: #262828;
    --gold: #c9a36f;
    --paper: #f7f7f5;
    --white: #ffffff;
    --text-dark: #1c1c1c;
  }
  * { box-sizing: border-box; margin: 0; padding: 0; }
  html, body { width: 1200px; height: 852px; overflow: hidden; }
  body {
    background: var(--bg);
    font-family: "Roboto", Arial, sans-serif;
    position: relative;
  }
  .card {
    position: absolute;
    width: 540px;
    height: 310px;
    border-radius: 18px;
    overflow: hidden;
    box-shadow: 0 6px 16px rgba(0,0,0,0.18);
    top: 271px;
  }

  /* Front */
  .card--front { left: 40px; background: var(--ink); }
  .card--front .wordmark {
    position: absolute; left: 0; right: 0; top: 110px;
    display: flex; justify-content: center; align-items: center; gap: 14px;
  }
  .wordmark__square { width: 18px; height: 18px; background: var(--gold); flex: none; }
  .wordmark__name {
    font-family: "Cinzel", Georgia, serif; font-weight: 600;
    font-size: 28px; letter-spacing: 3px; text-transform: uppercase;
    color: var(--white); white-space: nowrap;
  }
  .card--front .website {
    position: absolute; left: 0; right: 0; bottom: 26px;
    text-align: center; color: var(--white); font-size: 13px; letter-spacing: 0.3px;
  }
  .card--front .website span { color: var(--gold); }

  /* Back */
  .card--back { left: 620px; background: var(--paper); }
  .card--back .wordmark {
    position: absolute; left: 34px; top: 42px;
    display: flex; align-items: center; gap: 12px;
  }
  .card--back .wordmark__name { color: var(--text-dark); font-size: 24px; }
  .band {
    position: absolute; left: 0; top: 128px; width: 370px; height: 128px;
    background: var(--gold);
  }
  .badge-panel {
    position: absolute; left: 370px; top: 84px; width: 170px; height: 172px;
    background: var(--ink);
    display: flex; align-items: center; justify-content: center;
  }
  .badge { width: 104px; height: 104px; border-radius: 50%; background: var(--white); }
  .contact {
    position: absolute; left: 30px; top: 140px; width: 334px;
    color: var(--text-dark);
  }
  .contact__name { font-size: 20px; font-weight: 700; line-height: 24px; }
  .contact__title { font-size: 13px; line-height: 16px; margin-top: 2px; }
  .contact__row {
    display: flex; align-items: center; gap: 8px;
    font-size: 13px; line-height: 16px; margin-top: 7px; white-space: nowrap;
  }
  .contact__row svg { width: 13px; height: 13px; fill: var(--text-dark); flex: none; }
  .card--back .website {
    position: absolute; left: 30px; bottom: 20px;
    font-size: 13px; color: var(--text-dark);
  }
</style>
</head>
<body>
  <section class="card card--front" aria-label="Business card front">
    <div class="wordmark">
      <span class="wordmark__square"></span>
      <span class="wordmark__name">Kestrel Building Works</span>
    </div>
    <p class="website">www.<span>kestrelbuildingworks-example</span>.co.nz</p>
  </section>

  <section class="card card--back" aria-label="Business card back">
    <div class="wordmark">
      <span class="wordmark__square"></span>
      <span class="wordmark__name">Kestrel Building Works</span>
    </div>
    <div class="band"></div>
    <div class="badge-panel"><div class="badge" role="img" aria-label="Certified Framing Guild badge"></div></div>
    <div class="contact">
      <p class="contact__name">Malcolm Tivey</p>
      <p class="contact__title">Director</p>
      <p class="contact__row">
        <svg viewBox="0 0 24 24" aria-hidden="true"><path d="M6.6 10.8a15.1 15.1 0 0 0 6.6 6.6l2.2-2.2c.3-.3.7-.4 1-.2 1.1.4 2.3.6 3.6.6.6 0 1 .4 1 1V20c0 .6-.4 1-1 1C10.6 21 3 13.4 3 4c0-.6.4-1 1-1h3.5c.6 0 1 .4 1 1 0 1.3.2 2.5.6 3.6.1.3 0 .7-.2 1z"/></svg>
        0218845126
      </p>
      <p class="contact__row">
        <svg viewBox="0 0 24 24" aria-hidden="true"><path d="M2 5h20v14H2zM4 7v.5l8 5 8-5V7l-8 5z"/></svg>
        kestrelbuild.nz@maildrop-example.co.nz
      </p>
    </div>
    <p class="website">www.kestrelbuildingworks-example.co.nz</p>
  </section>
</body>
</html>
```